Building company needs a letterhead design

I'm after a modern but professional letter head.
Must have the below details:
- Logo
- Website - TARVELGROUP.COM.AU
- Email - INFO@TARVELGROUP.COM.AU
- Office - 03 58206317
- Mobile number - 0413865290
- ABN - 47 318 264 105
...........................................................................................................................................................................................................................
- Logo
- Office - 03 58206317
- ABN - 47 318 264 105

Target Market(s)

.

Industry/Entity Type

Construction Company

Font styles to use
Sans Serif

Requirements
Must have
• Must have the below details:
• - Logo
• - Website - TARVELGROUP.COM.AU
• - Email - INFO@TARVELGROUP.COM.AU
• - Office - 03 58206317
• - Mobile number - 0413865290
• - ABN - 47 318 264 105
Nice to have
• .
Should not have
• .

```html
<!DOCTYPE html>
<html lang="en">
<head>
<meta charset="utf-8">
<title>Tarvel Building Group Letterhead</title>
<link rel="stylesheet" href="https://fonts.googleapis.com/css2?family=Roboto+Condensed:wght@400;700&display=swap">
<style>
  :root {
    --charcoal: #2a2a2a;
    --gold: #f6b21a;
    --gold-light: #fbd270;
    --mist: #ececec;
    --paper: #ffffff;
    --ink: #1e1e1e;
  }
  html, body { margin: 0; padding: 0; overflow: hidden; background: var(--paper); }
  .letterhead {
    position: relative;
    width: 849px;
    height: 1200px;
    overflow: hidden;
    background: var(--paper);
    font-family: "Roboto Condensed", Arial, sans-serif;
  }
  .backdrop { position: absolute; inset: 0; }
  .brand {
    position: absolute;
    left: 62px;
    top: 42px;
    display: flex;
    align-items: center;
    gap: 14px;
  }
  .brand-square { width: 52px; height: 52px; background: var(--gold); flex: none; }
  .brand-name {
    display: flex;
    flex-direction: column;
    color: var(--paper);
    font-weight: 700;
    line-height: 1;
  }
  .brand-name .word-main { font-size: 40px; letter-spacing: 1.5px; }
  .brand-name .word-sub { font-size: 15.5px; letter-spacing: 1.4px; margin-top: 2px; }
  .header-details {
    position: absolute;
    right: 52px;
    top: 50px;
    text-align: right;
    font-size: 15px;
    line-height: 17px;
    letter-spacing: 0.2px;
  }
  .header-details .web, .header-details .abn { color: var(--gold); }
  .header-details .licence { color: var(--paper); }
  .footer-mark {
    position: absolute;
    left: 408px;
    top: 1048px;
    width: 34px;
    height: 40px;
    background: var(--gold);
  }
  .footer-contacts {
    position: absolute;
    left: 0;
    right: 0;
    top: 1150px;
    text-align: center;
    color: var(--ink);
    font-weight: 700;
    font-size: 15px;
    letter-spacing: 0.3px;
  }
</style>
</head>
<body>
<div class="letterhead">
  <svg class="backdrop" width="849" height="1200" viewBox="0 0 849 1200" aria-hidden="true">
    <polygon points="0,100 849,100 849,430" fill="var(--mist)"/>
    <polygon points="0,128 849,392 849,410 0,146" fill="var(--paper)"/>
    <polygon points="0,160 849,430 849,436 0,166" fill="var(--paper)"/>
    <rect x="0" y="0" width="849" height="112" fill="var(--charcoal)"/>
    <polygon points="0,1108 849,1124 849,1132 0,1132" fill="var(--gold-light)"/>
    <rect x="0" y="1128" width="849" height="72" fill="var(--gold)"/>
  </svg>

  <header>
    <div class="brand">
      <span class="brand-square"></span>
      <span class="brand-name">
        <span class="word-main">TARVEL</span>
        <span class="word-sub">BUILDING GROUP</span>
      </span>
    </div>
    <div class="header-details">
      <div class="web">WWW.TARVELGROUP.COM.AU</div>
      <div class="licence">REGISTERED BUILDING PRACTITIONER</div>
      <div class="abn">ABN: 47 318 264 105</div>
    </div>
  </header>

  <footer>
    <span class="footer-mark"></span>
    <div class="footer-contacts">OFFICE PHONE: 03 58206317 | MOBILE NUMBER: 0413865290 | EMAIL: INFO@TARVELGROUP.COM.AU</div>
  </footer>
</div>
</body>
</html>
```